Sales Flyer

I am looking for a one page 8x11 flyer that I can print and mail to potential customers. I want to get the message across to potential customers that if they purchase a mobile patrol service with my company then I will provide them with a free camera system with installation or intrusion alarm system with install.

I don't photos to add to the flyer but I would like to to have a couple of security related photos. Can the designers obtain applicable photos?

```html
<!DOCTYPE html>
<html lang="en">
<head>
<meta charset="utf-8">
<title>Northgate Security Group – Sales Flyer</title>
<link rel="stylesheet" href="https://fonts.googleapis.com/css2?family=Oswald:wght@400;500;600&family=Source+Sans+3:wght@400;600;700&display=swap">
<style>
  :root{
    --blue:#1566b0;
    --blue-deep:#0d4c8c;
    --cyan:#1e9ad6;
    --ink:#111418;
    --dark:#1c1f24;
    --dark-2:#2c3036;
    --grey-text:#4a4f55;
    --panel:#f1f2f4;
    --white:#ffffff;
    --silver:#c9ccd0;
  }
  *{box-sizing:border-box;margin:0;padding:0}
  html,body{width:1004px;height:1200px;overflow:hidden;background:#fff}
  body{font-family:"Source Sans 3",Arial,sans-serif;color:var(--ink)}
  .flyer{position:relative;width:1004px;height:1200px;overflow:hidden;background:var(--white)}

  .hero-photo{position:absolute;left:0;top:0;width:1004px;height:520px;
    background:linear-gradient(100deg,#ffffff 0%,#eef3f9 28%,#b9cde6 52%,#6f93c2 75%,#4c74ab 100%)}
  .brand{position:absolute;left:69px;top:62px;display:flex;align-items:center;gap:14px}
  .brand-dot{width:22px;height:22px;background:var(--blue)}
  .brand-name{font-family:"Oswald",sans-serif;font-weight:600;color:var(--blue);font-size:34px;line-height:1.05;letter-spacing:1px;text-transform:uppercase}

  .headline{position:absolute;left:52px;top:226px;font-family:"Oswald",sans-serif;font-weight:500;
    font-size:46px;line-height:58px;color:var(--ink);text-transform:uppercase;letter-spacing:.3px;white-space:nowrap}

  .swoosh{position:absolute;left:0;top:440px;width:1004px;height:110px}

  .side-panel{position:absolute;left:560px;top:404px;width:444px;height:640px;
    background:linear-gradient(180deg,var(--dark-2),var(--dark))}
  .circle-photo{position:absolute;border-radius:50%;border:6px solid #d9dde2;box-shadow:0 3px 8px rgba(0,0,0,.35)}
  .circle-photo.camera{left:636px;top:356px;width:140px;height:140px;background:radial-gradient(circle at 40% 40%,#c8a16a,#4a3421)}
  .circle-photo.monitors{left:793px;top:330px;width:194px;height:194px;background:radial-gradient(circle at 50% 45%,#8fa8bf,#2f3a46 70%,#18120d)}

  .why-tab{position:absolute;left:565px;top:577px;width:439px;height:42px;
    background:linear-gradient(90deg,var(--blue),var(--cyan));color:#fff;white-space:nowrap;overflow:hidden;
    font-family:"Oswald",sans-serif;font-weight:500;font-size:18px;line-height:42px;padding-left:18px;text-transform:uppercase;letter-spacing:.2px}
  .why-list{position:absolute;left:596px;top:640px;width:390px;list-style:none;color:#e9ecef;font-size:17px;line-height:20px}
  .why-list li{position:relative;padding-left:28px;margin-bottom:16px}
  .why-list svg{position:absolute;left:0;top:2px}
  .contact-cta{position:absolute;left:580px;top:905px;width:410px;text-align:center;color:var(--cyan);
    font-weight:700;font-size:19px;line-height:24px;text-transform:uppercase}

  .contact-box{position:absolute;left:567px;top:995px;width:437px;height:205px;
    background:linear-gradient(135deg,var(--cyan),var(--blue) 70%,var(--blue-deep));color:#fff;padding:38px 0 0 26px}
  .contact-title{font-family:"Oswald",sans-serif;font-size:23px;font-weight:400;text-transform:uppercase;margin-bottom:14px}
  .contact-line{display:flex;align-items:center;gap:12px;font-weight:600;font-size:17px;margin-bottom:12px}
  .badge{position:absolute;left:880px;top:1012px;width:98px;height:98px;border-radius:50%;
    background:radial-gradient(circle at 35% 30%,#f4f5f6,var(--silver) 60%,#8c9096);
    display:flex;align-items:center;justify-content:center;text-align:center;
    font-family:"Oswald",sans-serif;font-weight:600;font-size:13px;line-height:15px;color:#fff;text-transform:uppercase;
    text-shadow:0 1px 1px rgba(0,0,0,.35);transform:rotate(-8deg)}

  .offer-intro{position:absolute;left:41px;top:580px;width:480px;font-weight:700;font-size:18.5px;line-height:25px;text-transform:uppercase;color:var(--ink)}
  .offer-intro .accent{color:var(--blue)}

  .system-card{position:absolute;left:41px;width:500px;height:190px;background:var(--panel);
    box-shadow:0 2px 6px rgba(0,0,0,.25);border-bottom:12px solid var(--blue)}
  .system-card.cameras{top:716px}
  .system-card.alarm{top:928px}
  .card-tab{position:absolute;right:0;top:0;width:300px;height:40px;
    background:linear-gradient(90deg,var(--cyan),var(--blue));clip-path:polygon(8% 0,100% 0,100% 100%,0 100%);
    color:#fff;font-family:"Oswald",sans-serif;font-weight:500;font-size:20px;line-height:40px;text-align:right;padding-right:14px;text-transform:uppercase;white-space:nowrap}
  .product-photo{position:absolute;left:22px;top:30px;width:190px;height:130px;
    background:radial-gradient(ellipse at center,#ffffff,#d5d8dc)}
  .card-text{position:absolute;left:224px;top:68px;width:260px;color:var(--grey-text);font-size:19px;line-height:23px}
  .system-card.alarm .card-text{top:60px}

  .call-bar{position:absolute;left:0;top:1138px;width:567px;height:62px;background:linear-gradient(180deg,var(--dark-2),var(--dark));
    display:flex;align-items:center;justify-content:center;gap:22px;color:#fff;font-family:"Oswald",sans-serif;font-size:30px;letter-spacing:1px;text-transform:uppercase}
  .call-bar::before{content:"";position:absolute;left:0;top:-8px;width:567px;height:4px;background:linear-gradient(90deg,#d5d8dc,#8c9096)}
</style>
</head>
<body>
<main class="flyer">
  <div class="hero-photo" role="img" aria-label="Businessman in a suit holding his hand above a glowing shield with a padlock, over a blue digital background"></div>

  <div class="brand">
    <span class="brand-dot"></span>
    <span class="brand-name">Northgate<br>Security Group</span>
  </div>

  <h1 class="headline">Does your business<br>currently use security<br>guards or mobile patrols?</h1>

  <svg class="swoosh" viewBox="0 0 1004 110" preserveAspectRatio="none" aria-hidden="true">
    <path d="M0 0 L0 60 L440 110 L1004 40 L1004 110 L0 110 Z" fill="#ffffff"/>
    <path d="M0 6 C150 40 320 70 440 92 L 560 66 L440 80 C320 58 150 30 0 18 Z" fill="var(--blue)"/>
    <path d="M0 22 C150 42 320 66 440 86 L440 92 C320 72 150 50 0 30 Z" fill="var(--cyan)" opacity=".7"/>
  </svg>

  <section class="side-panel" aria-hidden="true"></section>
  <div class="circle-photo camera" role="img" aria-label="Ceiling-mounted security cameras in warm light"></div>
  <div class="circle-photo monitors" role="img" aria-label="Control room with a wall of surveillance monitors"></div>

  <h2 class="why-tab">Why partner with Northgate Security Group</h2>
  <ul class="why-list">
    <li><svg width="16" height="16" viewBox="0 0 16 16"><circle cx="8" cy="8" r="7" fill="none" stroke="#fff" stroke-width="1.5"/><path d="M4.5 8.2 7 10.5 11.5 5.5" fill="none" stroke="#fff" stroke-width="1.8"/></svg>We specialize in both security personnel and security system installations.</li>
    <li><svg width="16" height="16" viewBox="0 0 16 16"><circle cx="8" cy="8" r="7" fill="none" stroke="#fff" stroke-width="1.5"/><path d="M4.5 8.2 7 10.5 11.5 5.5" fill="none" stroke="#fff" stroke-width="1.8"/></svg>All of our security guard and mobile patrol services come with access to our online reporting software. Contact us for a free demo to see how our software can help you.</li>
    <li><svg width="16" height="16" viewBox="0 0 16 16"><circle cx="8" cy="8" r="7" fill="none" stroke="#fff" stroke-width="1.5"/><path d="M4.5 8.2 7 10.5 11.5 5.5" fill="none" stroke="#fff" stroke-width="1.8"/></svg>Our responsiveness to clients is unmatched.</li>
    <li><svg width="16" height="16" viewBox="0 0 16 16"><circle cx="8" cy="8" r="7" fill="none" stroke="#fff" stroke-width="1.5"/><path d="M4.5 8.2 7 10.5 11.5 5.5" fill="none" stroke="#fff" stroke-width="1.8"/></svg>Our mobile service includes free alarm responses.</li>
  </ul>
  <p class="contact-cta">Contact us today to discuss<br>how we can help you with your<br>security needs.</p>

  <section class="contact-box">
    <h3 class="contact-title">Contact us</h3>
    <p class="contact-line"><svg width="14" height="14" viewBox="0 0 24 24"><path fill="#fff" d="M6.6 10.8a15 15 0 0 0 6.6 6.6l2.2-2.2c.3-.3.7-.4 1-.2 1.1.4 2.3.6 3.6.6.6 0 1 .4 1 1V20c0 .6-.4 1-1 1A17 17 0 0 1 3 4c0-.6.4-1 1-1h3.5c.6 0 1 .4 1 1 0 1.3.2 2.5.6 3.6.1.3 0 .7-.2 1z"/></svg>780.555.0142</p>
    <p class="contact-line"><svg width="14" height="14" viewBox="0 0 24 24"><path fill="#fff" d="M2 5h20v14H2z"/><path d="M2 5l10 8 10-8" fill="none" stroke="#1566b0" stroke-width="2"/></svg>sam@northgatesecurity.com</p>
    <p class="contact-line"><svg width="14" height="14" viewBox="0 0 24 24"><circle cx="12" cy="12" r="10" fill="none" stroke="#fff" stroke-width="2"/><path d="M2 12h20M12 2c3 3 3 17 0 20M12 2c-3 3-3 17 0 20" fill="none" stroke="#fff" stroke-width="1.6"/></svg>NorthgateSecurity.com</p>
  </section>
  <div class="badge">Serving<br>all of<br>Alberta</div>

  <p class="offer-intro"><span class="accent">Partner with Northgate Security Group</span> for your guard or mobile services and receive one of the following security systems with installation free of charge.</p>

  <article class="system-card cameras">
    <h3 class="card-tab">Free security systems</h3>
    <div class="product-photo" role="img" aria-label="White dome security camera above a network video recorder"></div>
    <p class="card-text">Clearline 6 high resolution security camera system with a 2TB NVR.</p>
  </article>

  <article class="system-card alarm">
    <h3 class="card-tab">Free security systems</h3>
    <div class="product-photo" role="img" aria-label="Alarm keypad, control panel, motion sensors, door contacts and key fob"></div>
    <p class="card-text">Sentrix intrusion alarm system with motion sensors, door contacts and glass break detectors.</p>
  </article>

  <div class="call-bar">
    <span>Call us now</span>
    <svg width="26" height="26" viewBox="0 0 24 24" aria-hidden="true"><path fill="#fff" d="M6.6 10.8a15 15 0 0 0 6.6 6.6l2.2-2.2c.3-.3.7-.4 1-.2 1.1.4 2.3.6 3.6.6.6 0 1 .4 1 1V20c0 .6-.4 1-1 1A17 17 0 0 1 3 4c0-.6.4-1 1-1h3.5c.6 0 1 .4 1 1 0 1.3.2 2.5.6 3.6.1.3 0 .7-.2 1z"/></svg>
    <span>780.555.0142</span>
  </div>
</main>
</body>
</html>
```